Label design for high quality nutritional supplement brand

We need a new label design for our dietary supplement brand "NorlumPlus" from Germany. We sell high-quality nutritional supplements that help improve overall well-being.

All products in our range should receive the new label. You can find our current design on our homepage norlumplus-shop.example. The new design should be completely redesigned and look modern, fresh, high quality, minimalist and clean. We prefer the colors nude, green and earth tones.

The newly created label should contain our NorlumPlus logo. For this reason you will find this file attached. You will also find our current label, which needs to be renewed, in the appendix.

Colors

Designer to choose colors to be used in the design.

Requirements
Must have
• NorlumPlus logo

```html
<!DOCTYPE html>
<html lang="de">
<head>
<meta charset="utf-8">
<title>NorlumPlus – Etikett Rückseite</title>
<link href="https://fonts.googleapis.com/css2?family=Open+Sans:wght@400;600&display=swap" rel="stylesheet">
<style>
  :root {
    --page-bg: #e8e9eb;
    --label-bg: #fbfbfb;
    --olive: #b5b254;
    --olive-dark: #6e6b1a;
    --olive-light: #b9b654;
    --text: #222222;
    --band-text: #f3f0d8;
  }
  * { margin: 0; padding: 0; box-sizing: border-box; }
  html, body {
    width: 1121px;
    height: 1200px;
    overflow: hidden;
    background: var(--page-bg);
    font-family: "Open Sans", Arial, sans-serif;
  }
  .label {
    position: absolute;
    left: 152px;
    top: 72px;
    width: 816px;
    height: 1056px;
    background: var(--label-bg);
    overflow: hidden;
    box-shadow: 0 2px 12px rgba(0,0,0,0.06);
  }
  .accent-stripe {
    position: absolute;
    left: 0;
    top: 0;
    width: 816px;
    height: 1056px;
  }
  .info-box {
    position: absolute;
    left: 50px;
    width: 694px;
    border: 1.5px solid var(--olive);
    background: var(--label-bg);
    padding: 10px 16px;
    color: var(--text);
    font-size: 25.5px;
    line-height: 31px;
    white-space: nowrap;
  }
  .info-box--usage { top: 60px; height: 82px; }
  .info-box--notice { top: 182px; height: 206px; }
  .info-box--ingredients { top: 425px; height: 448px; padding-top: 14px; }
  .storage-band {
    position: absolute;
    left: 0;
    bottom: 0;
    width: 816px;
    height: 130px;
    background: linear-gradient(90deg, var(--olive-dark) 0%, var(--olive-light) 45%, var(--olive-light) 100%);
    color: var(--band-text);
    font-size: 26.5px;
    font-weight: 600;
    line-height: 31px;
    padding: 30px 56px;
    white-space: nowrap;
  }
</style>
</head>
<body>
  <main class="label">
    <svg class="accent-stripe" viewBox="0 0 816 1056" aria-hidden="true">
      <polygon points="566,388 662,388 816,450 816,540" fill="var(--olive)"/>
    </svg>

    <section class="info-box info-box--usage">
      Verzehrempfehlung: Täglich 2 Kapseln mit<br>
      ausreichend Flüssigkeit einnehmen.
    </section>

    <section class="info-box info-box--notice">
      Die angegebene empfohlene tägliche Verzehrmenge<br>
      darf nicht überschritten werden. Nahrungsergän-<br>
      zungs-mittel sind kein Ersatz für eine abwechslungsrei-<br>
      che und ausgewogene Ernährung und eine gesunde<br>
      Lebens-weise. Außerhalb der Reichweite von Kindern<br>
      aufbewahren.
    </section>

    <section class="info-box info-box--ingredients">
      Zutaten: Inulin (46%), Bakterienkulturen (Lactobacillus<br>
      acidophilus, Lactobacillus plantarum, Lactobacillus<br>
      casei, Bifidobacterium breve, Bifidobacterium longum,<br>
      Bifidobacterium lactis, Bifidobacterium bifidum,<br>
      Streptococcus thermophilus, Lactobacillus crispatus,<br>
      Lactobacillus gasseri, Lactobacillus bulgaricus,<br>
      Bifidobacterium infantis, Lactobacillus rhamnosus,<br>
      Lactobacillus salivarius, Lactobacillus paracasei,<br>
      Lactobacillus reuteri, Lactobacillus fermentum,<br>
      Lactococcus lactis, Lactobacillus johnsonii,<br>
      Pediococcus acidilactici, Bifidobacterium animalis),<br>
      Überzugmittel: Hydroxypropylmethylcellulose.<br>
      Kapselhülle: vegan
    </section>

    <footer class="storage-band">
      Ungeöffnet, kühl und trocken aufbewahrt,<br>
      mindestens haltbar bis Ende / L-Nr.: siehe Bodenaufdruck
    </footer>
  </main>
</body>
</html>
```